Plumbing Website

Design a simple 4 page website based on our provided logo and sketches. Winning designer should be willing to upgrade as needed (for additional fee). A design that includes SEO features is a plus.
I would like to see Home, , Services, Recent Jobs (set up for pictures), Contact. I like the water dropplet back ground. Please dont put logo in a box. File attached as exaple only, I am looking for a request service now button in the middle that will have a form fill to be emailed to two different addresses,
I would like to see vibrant colors. Examples of sites I like are www.maplewickplumbingandheat.com look also at www.kfv-fernvalleyplumbing.com - this site is too busy but has good seo features.

```html
<!DOCTYPE html>
<html lang="en">
<head>
<meta charset="utf-8">
<title>Sierra Creek Plumbing — Home</title>
<link href="https://fonts.googleapis.com/css2?family=Varela+Round&family=Arimo:wght@400;700&display=swap" rel="stylesheet">
<style>
:root{
  --water-1:#2aa6e6;
  --water-2:#bfe9fb;
  --brand-blue:#0d4f9c;
  --nav-blue:#0a73b5;
  --accent-red:#e0141e;
  --text:#222;
  --muted:#666;
  --panel:#fff;
  --footer-bg:#f4f4f4;
  --dark-btn:#333;
}
*{box-sizing:border-box;margin:0;padding:0}
html,body{width:1007px;height:1200px;overflow:hidden}
body{position:relative;font-family:"Arimo",Arial,sans-serif;color:var(--text)}
.backdrop{position:absolute;inset:0;background:
  repeating-linear-gradient(90deg,var(--water-2) 0 40px,var(--water-1) 60px,var(--water-2) 100px);}
.page{position:absolute;left:86px;top:15px;width:836px;height:1175px;background:var(--panel);box-shadow:0 0 6px rgba(0,0,0,.3)}
.abs{position:absolute}
.brand{left:18px;top:30px;display:flex;align-items:center;gap:8px;font-family:"Varela Round",sans-serif;font-size:22px;color:var(--brand-blue)}
.brand .dot{width:14px;height:14px;border-radius:50%;background:var(--brand-blue)}
.phone{right:20px;top:8px;font-size:19px;color:#333}
.follow{right:140px;top:62px;font:italic 11px Georgia,serif;color:#333;white-space:nowrap}
.socials{right:20px;top:55px;display:flex;gap:4px}
.socials span{width:24px;height:23px;background:#2c6fc0;border-radius:2px}
.socials span:nth-child(2){background:#32a3e6}
.socials span:nth-child(3){background:#6aa84f}
.socials span:nth-child(4){background:#f07a1a}
.nav{left:459px;top:92px;display:flex;font-size:12px}
.nav a{color:#222;text-decoration:none;padding:3px 11px;margin-right:10px}
.nav a.active{background:var(--nav-blue);color:#fff;border-radius:2px 2px 0 0}
.nav-rule{left:0;top:111px;width:836px;height:4px;background:var(--nav-blue)}
.hero{left:9px;top:124px;width:818px;height:316px;background:linear-gradient(100deg,#3b6aa8 0%,#8fa9c9 40%,#e6e8ea 70%,#cfd3d6 100%)}
.arrow{top:138px;width:38px;height:38px}
.request{left:625px;top:237px;width:156px;height:57px;background:#000;border:2px solid #fff;border-radius:10px;box-shadow:0 0 0 1px #000;text-align:center;font-family:"Varela Round",sans-serif}
.request b{display:block;color:var(--accent-red);font-size:19px;margin-top:8px;letter-spacing:1px}
.request i{display:block;font-style:normal;color:#fff;font-size:14px;letter-spacing:.5px}
.rule{left:29px;width:773px;height:1px;background:#ccc}
.intro{left:20px;top:485px;width:797px;text-align:center}
.intro h1{font-family:"Varela Round",sans-serif;font-weight:400;color:var(--accent-red);font-size:22px;letter-spacing:1px;margin-bottom:8px}
.intro p{font-size:10.5px;line-height:15px;margin-bottom:15px}
.btn{background:var(--dark-btn);color:#fff;font-weight:700;font-size:10.5px;padding:4px 9px;display:inline-block}
.service{top:696px;width:205px}
.service h2{font-family:"Varela Round",sans-serif;font-weight:400;color:var(--brand-blue);font-size:20px;letter-spacing:.5px;white-space:nowrap}
.service h3{font-family:"Varela Round",sans-serif;font-weight:400;color:#777;font-size:11px;margin:0 0 9px 2px}
.thumb{width:203px;height:109px;border:1px solid #ddd;padding:5px;background:#fff}
.thumb div{width:100%;height:100%}
.service p{font-size:9.3px;line-height:15px;color:#333;margin-top:11px;text-align:justify;letter-spacing:.2px}
.vsep{top:690px;height:226px;border-left:1px dotted #bbb}
.footer{left:0;top:926px;width:836px;height:202px;background:var(--footer-bg)}
.about{left:29px;top:14px;font-size:10.3px;line-height:15px;color:#444;letter-spacing:.2px}
.about h4{font-family:"Varela Round",sans-serif;font-weight:400;font-size:15px;color:#666;margin-bottom:10px;letter-spacing:.5px}
.about b{color:#555;display:block;margin-top:9px}
.profile{left:286px;top:20px;width:268px;font-size:10.3px;line-height:15px;color:#333;text-align:justify}
.profile h4{font-family:"Varela Round",sans-serif;font-weight:400;font-size:15px;color:#666;margin-bottom:14px;letter-spacing:.5px}
.fsep{top:14px;height:180px;border-left:1px dotted #bbb}
.enquiry{left:619px;top:16px;width:193px;height:186px}
.enquiry h4{font-family:"Varela Round",sans-serif;font-weight:400;font-size:21px;color:var(--brand-blue);margin:0 0 14px 5px;letter-spacing:.5px}
.field{background:#fff;border:1px solid #ddd;border-radius:3px;font-size:9.5px;color:#555;padding:5px 9px;margin-bottom:9px;height:23px}
.field.tall{height:56px;line-height:15px}
.submit{position:absolute;right:2px;top:166px}
.bottom-nav{left:0;top:1142px;width:836px;text-align:center;font-size:9.5px;color:#333;word-spacing:2px}
.copyright{left:0;top:1157px;width:836px;text-align:center;font-size:9.5px;color:#333}
</style>
</head>
<body>
<div class="backdrop" role="img" aria-label="Blue water droplet background"></div>
<div class="page">
  <header>
    <div class="abs brand"><span class="dot"></span>Sierra Creek Plumbing</div>
    <div class="abs phone">Call 951-555-0142</div>
    <div class="abs follow">Follow us on:</div>
    <div class="abs socials" aria-label="Social links"><span></span><span></span><span></span><span></span></div>
    <nav class="abs nav"><a class="active" href="#">Home</a><a href="#">Services</a><a href="#">Recent Jobs</a><a href="#">Contact</a></nav>
    <div class="abs nav-rule"></div>
  </header>

  <section class="abs hero" role="img" aria-label="Smiling plumber in cap beside sink pipework">
    <svg class="abs arrow" style="left:2px" viewBox="0 0 38 38"><circle cx="19" cy="19" r="17" fill="none" stroke="#ccc" stroke-width="3"/><path d="M23 11 L13 19 L23 27Z" fill="#ccc"/></svg>
    <svg class="abs arrow" style="right:2px" viewBox="0 0 38 38"><circle cx="19" cy="19" r="17" fill="none" stroke="#ccc" stroke-width="3"/><path d="M15 11 L25 19 L15 27Z" fill="#ccc"/></svg>
    <div class="abs request"><b>REQUEST</b><i>service now</i></div>
  </section>

  <div class="abs rule" style="top:473px"></div>
  <section class="abs intro">
    <h1>Our Family Serving Your Family</h1>
    <p>Sierra Creek Plumbing is the industry leader in the area. We are a Plumbing, Drain Cleaning, and General Engineering contractors, providing excellent customer service and helping homeowners to live more comfortable and healthy lives. If you are looking for a Plumber in Cedar Valley then call on Sierra Creek Plumbing as your Plumbing Contractor. When the water heater bursts or the bathroom is flooding, do you want the best plumber available, or do you want the cheapest? At Sierra Creek Plumbing,</p>
    <p>we know that the best plumber does world-class work, is fully licensed and insured, is available 24/7 – including during emergencies – and somehow combines world-class equipment and service with world-class affordability.</p>
    <span class="btn">Readmore</span>
  </section>
  <div class="abs rule" style="top:668px"></div>

  <article class="abs service" style="left:44px">
    <h2 style="margin-left:3px">Plumbing</h2><h3 style="margin-left:5px">simply dummy text</h3>
    <div class="thumb"><div role="img" aria-label="Plumber working at a bathroom faucet" style="background:linear-gradient(120deg,#c9b89a,#2b3550)"></div></div>
    <p>We are a full-service plumbing company. Our plumbers are experts at repairing or replacing all types of leaks,</p>
  </article>
  <div class="abs vsep" style="left:278px"></div>
  <article class="abs service" style="left:308px">
    <h2 style="margin-left:11px">Drain Cleaning</h2><h3 style="margin-left:13px">simply dummy text</h3>
    <div class="thumb"><div role="img" aria-label="Plumber fixing pipes under a sink" style="background:linear-gradient(120deg,#3a5f9c,#e3e3e3)"></div></div>
    <p>We have been cleaning drains for almost 20 years. Whether it's a kitchen sink or a main sewer line stoppage,</p>
  </article>
  <div class="abs vsep" style="left:547px"></div>
  <article class="abs service" style="left:578px">
    <h2 style="margin-left:5px">General Engineering</h2><h3 style="margin-left:7px">simply dummy text</h3>
    <div class="thumb"><div role="img" aria-label="Road crew cutting asphalt with traffic cones" style="background:linear-gradient(180deg,#9fb3c4,#6b6a66)"></div></div>
    <p>What sets us apart, is being a class “A” engineering contractor. On larger projects that require cutting concrete and asphalt,</p>
  </article>

  <footer class="abs footer">
    <div class="abs about">
      <h4>About Us</h4>
      <b style="margin-top:0">Our Office:</b>4280 Larkspur Ave Suite 210<br>Pine Hollow, CA 91700
      <b>Contact Info:</b>951-555-0142<br>service@sierracreekplumbing.com
      <b>24 Hours a Day</b>7 Days a Week
    </div>
    <div class="abs fsep" style="left:265px"></div>
    <div class="abs profile">
      <h4>Company Profile</h4>
      When the water heater bursts or the bathroom is flooding, do you want the best plumber available, or do you want the cheapest? At Sierra Creek Plumbing, we know that the best plumber does world-class work, is fully licensed and insured, is available 24/7 – including during emergencies – and somehow combines world-class equipment and service with world-class affordability.
    </div>
    <div class="abs fsep" style="left:579px"></div>
    <form class="abs enquiry">
      <h4>Quick Enquiry</h4>
      <div class="field">Your Name</div>
      <div class="field">Email</div>
      <div class="field tall">Tell Us About Your Project and your Requirment</div>
      <span class="btn submit">Submit</span>
    </form>
  </footer>
  <div class="abs bottom-nav">Home &nbsp; ~ &nbsp; Services &nbsp; ~ &nbsp; Recent Jobs &nbsp; ~ &nbsp; Contact</div>
  <div class="abs copyright">Copyright © Sierra Creek Plumbing . All Rights Reserved</div>
</div>
</body>
</html>
```